Bottle Label for Premium Gold CBD Oil

10 ml CBD-Oil bottle. The job is pretty straight forward and everything you need is prepared. However, the design part of the creative part ^^ The design of a lot of follow-up products we could do together. We thought about an exclusive / minimalist approach to Brindle. The bottle itself is delivered in a drawer box which looks much better than the cheap packages of the competition. Everything about the product is supposed to be honest and of high quality. The product is even more cost-effective than CBD-Oils. Key feature of the product is its deeply golden color. The design should be in harmony with this color. The customer pays a high price for this little bottle and has high expectations. Accordingly, the label should express itself and the product is worth every cent. Which it is by the way. If you would like to see the labels of the competition, just type in "CBD OIL" on "varokel.de". However, we are currently the only ones with a new filtration and the corresponding golden color. This label is going to be the base of a whole series of products. If we are happy with your label design, we will do a lot of following up designs with you. The logo design is already done and just needs to be implemented. We are looking forward to your designs. Many, many thanks in advance
Target Market(s)
Customers who want to use the absolute top CBD product on the market in order to improve their health
Colors
Requirements
Must have
- Please read the pdf-file with detailed descriptions and pictures. The costomer should always see that our product is of the highest quality. Please feel free to stick to our suggestions / ideas since I we are no designers. If you have your own cool approach, just submit it ^^
Nice to have
- We think it would be nice to have a drop out on the front of the label. We could imagine an exclusive / minimalist approach similar to Brindle

```html
<!DOCTYPE html>
<html lang="de">
<head>
<meta charset="utf-8">
<title>10% CBD Oil – Premium Gold Label</title>
<link rel="stylesheet" href="https://fonts.googleapis.com/css2?family=Fira+Sans:wght@300;400&display=swap">
<style>
  :root {
    --backdrop: #f1f1f1;
    --label-paper: #fbfbf9;
    --label-edge: #e6e6e3;
    --ink-dark: #5a5a5a;
    --ink-mid: #7d7d7d;
    --ink-light: #979797;
    --gold-light: #f6e27a;
    --gold-deep: #e8c93a;
    --brand: #c98a2c;
  }
  * { margin: 0; padding: 0; box-sizing: border-box; }
  html, body {
    width: 994px;
    height: 1200px;
    overflow: hidden;
    background: var(--backdrop);
  }
  body {
    position: relative;
    font-family: "Fira Sans", sans-serif;
  }
  .label {
    position: absolute;
    left: 117px;
    top: 94px;
    width: 760px;
    height: 1012px;
    background: var(--label-paper);
    border: 1px solid var(--label-edge);
  }
  .brand {
    position: absolute;
    right: 44px;
    top: 60px;
    display: flex;
    align-items: center;
    gap: 12px;
    font-size: 34px;
    font-weight: 400;
    letter-spacing: 2px;
    color: var(--brand);
  }
  .brand-dot {
    width: 18px;
    height: 18px;
    border-radius: 50%;
    background: var(--brand);
  }
  .product-title {
    position: absolute;
    left: 40px;
    top: 218px;
    font-size: 54px;
    font-weight: 400;
    letter-spacing: 2px;
    color: var(--ink-dark);
  }
  .product-line {
    position: absolute;
    left: 42px;
    top: 304px;
    font-size: 36px;
    font-weight: 300;
    letter-spacing: 1px;
    color: var(--ink-mid);
  }
  .product-type {
    position: absolute;
    left: 42px;
    top: 370px;
    font-size: 28px;
    font-weight: 300;
    letter-spacing: 1px;
    color: var(--ink-light);
  }
  .drop {
    position: absolute;
    left: 272px;
    top: 372px;
    width: 248px;
    height: 476px;
  }
  .specs {
    position: absolute;
    left: 24px;
    right: 24px;
    top: 896px;
    text-align: center;
    font-size: 32px;
    font-weight: 300;
    color: var(--ink-mid);
    white-space: nowrap;
  }
</style>
</head>
<body>
  <main class="label">
    <div class="brand"><span class="brand-dot"></span>Aurelis</div>
    <h1 class="product-title">10% CBD OIL</h1>
    <p class="product-line">PREMIUM GOLD</p>
    <p class="product-type">VOLLSPEKTUM</p>
    <svg class="drop" viewBox="0 0 62 119" aria-hidden="true">
      <defs>
        <linearGradient id="gold-fill" x1="0" y1="0" x2="1" y2="1">
          <stop offset="0" stop-color="var(--gold-light)"/>
          <stop offset="1" stop-color="var(--gold-deep)"/>
        </linearGradient>
      </defs>
      <path d="M31 0 C33 20 62 55 62 88 A31 31 0 0 1 0 88 C0 55 29 20 31 0 Z" fill="url(#gold-fill)"/>
    </svg>
    <p class="specs">10 Ml | 250 Tropfen | 1000 Mg Cbd</p>
  </main>
</body>
</html>
```